Business Card Design Project

Hi

I have a draft of a business card which I need smarting up. I have attached the pdf of this.
The information on the front is correct.
The information on the back should contain:
Project Management, Consulting, Master Systems Integrator, Datacenter, Relocations, Restacks. I want this spiraling around the back

Can you change the telephone number to +65 8574 3916.
Updates

Target Market(s)

Chief Technology Officers of large multi-nationals

Industry/Entity Type

Business

Requirements
Must have
• My logo - Vorlith (attached)
The orange and blue colour running around the edge

```html
<!DOCTYPE html>
<html lang="en">
<head>
<meta charset="utf-8">
<title>Vorlith Business Card</title>
<link rel="stylesheet" href="https://fonts.googleapis.com/css2?family=Quicksand:wght@300&family=Oswald:wght@400;500&family=Crimson+Text&display=swap">
<style>
  :root {
    --stage: #e9eef2;
    --card-white: #ffffff;
    --grid-cyan: #5fdcf0;
    --grid-pale: #e8fafd;
    --ink-dark: #231f1e;
    --wordmark-grey: #5a5a5a;
    --accent-orange: #f0901e;
    --accent-blue: #2fd3e8;
    --bar-text: #ffffff;
  }
  * { margin: 0; padding: 0; box-sizing: border-box; }
  html, body { width: 1200px; height: 1200px; overflow: hidden; }
  body {
    background: var(--stage);
    display: flex; flex-direction: column; align-items: center; justify-content: center;
    gap: 50px;
  }
  .card {
    position: relative; width: 760px; height: 440px; overflow: hidden;
    background: var(--card-white);
    box-shadow: 0 6px 18px rgba(0,0,0,0.18);
  }
  .card::after {
    content: ""; position: absolute; inset: 0; pointer-events: none;
    box-shadow: inset 0 0 0 6px var(--accent-orange), inset 0 0 0 11px var(--accent-blue);
  }
  .card-texture { position: absolute; inset: 0; }
  .card-front .card-texture {
    background: linear-gradient(100deg, var(--card-white) 30%, var(--grid-pale) 55%, var(--grid-cyan) 100%);
    opacity: 0.75;
  }
  .card-back .card-texture {
    background: radial-gradient(ellipse at 25% 75%, var(--card-white) 10%, var(--grid-pale) 45%, var(--grid-cyan) 100%);
    opacity: 0.8;
  }
  .brand-square { position: absolute; background: var(--ink-dark); border-radius: 14px; }
  .brand-name {
    position: absolute; font-family: "Quicksand", sans-serif; font-weight: 300;
    color: var(--wordmark-grey); line-height: 1;
  }
  .card-front .brand-square { left: 60px; top: 70px; width: 170px; height: 170px; }
  .card-front .brand-name { left: 265px; top: 80px; font-size: 96px; }
  .person-name {
    position: absolute; left: 62px; top: 262px;
    font-family: "Oswald", sans-serif; font-weight: 500; font-size: 42px;
    color: var(--ink-dark); line-height: 1;
  }
  .person-role {
    position: absolute; left: 62px; top: 312px;
    font-family: "Oswald", sans-serif; font-weight: 400; font-size: 22px;
    color: var(--ink-dark); line-height: 1;
  }
  .contact-band {
    position: absolute; left: 0; right: 0; bottom: 0; height: 88px;
    background: var(--ink-dark);
    padding: 16px 24px 0 60px;
    font-family: "Crimson Text", serif; font-size: 17px; line-height: 1.45;
    color: var(--accent-orange);
  }
  .card-back .brand-square { left: 40px; top: 300px; width: 56px; height: 56px; border-radius: 8px; }
  .card-back .brand-name { left: 108px; top: 308px; font-size: 40px; }
  .service-fan { position: absolute; inset: 0; }
  .service-bar { fill: var(--ink-dark); }
  .service-label { font-family: "Oswald", sans-serif; font-size: 20px; fill: var(--bar-text); }
</style>
</head>
<body>
  <section class="card card-front">
    <div class="card-texture" role="img" aria-label="Fine cyan grid pattern fading into white"></div>
    <div class="brand-square"></div>
    <div class="brand-name">Vorlith</div>
    <div class="person-name">Marcus Delane</div>
    <div class="person-role">Director</div>
    <div class="contact-band">
      Vorlith Pte Ltd , 14 Harbour Crest , #05-11 Keppel Point Tower 2 , Singapore , W-www.vorlith.com<br>
      +65 8574 3916 , T-94826051 , E-marcus.delane@vorlith.com
    </div>
  </section>

  <section class="card card-back">
    <div class="card-texture" role="img" aria-label="Fine cyan grid pattern around a white centre"></div>
    <div class="brand-square"></div>
    <div class="brand-name">Vorlith</div>
    <svg class="service-fan" width="760" height="440" viewBox="0 0 760 440">
      <g transform="translate(190 120) rotate(-90)">
        <rect class="service-bar" x="-100" y="-21" width="200" height="42"/>
        <text class="service-label" x="0" y="7" text-anchor="middle">Relocations</text>
      </g>
      <g transform="translate(267 132) rotate(-72)">
        <rect class="service-bar" x="-100" y="-21" width="200" height="42"/>
        <text class="service-label" x="0" y="7" text-anchor="middle">Restacks</text>
      </g>
      <g transform="translate(337 168) rotate(-54)">
        <rect class="service-bar" x="-100" y="-21" width="200" height="42"/>
        <text class="service-label" x="0" y="7" text-anchor="middle">Datacenter</text>
      </g>
      <g transform="translate(421 202) rotate(-36)">
        <rect class="service-bar" x="-135" y="-21" width="270" height="42"/>
        <text class="service-label" x="0" y="7" text-anchor="middle">Master Systems Integrator</text>
      </g>
      <g transform="translate(428 293) rotate(-18)">
        <rect class="service-bar" x="-100" y="-21" width="200" height="42"/>
        <text class="service-label" x="0" y="7" text-anchor="middle">Consulting</text>
      </g>
      <g transform="translate(450 370)">
        <rect class="service-bar" x="-110" y="-21" width="220" height="42"/>
        <text class="service-label" x="0" y="7" text-anchor="middle">Project Management</text>
      </g>
    </svg>
  </section>
</body>
</html>
```